Business Cards, Stationery, Email signature
and Stationary
Business Cards, Stationery, Email signature - Construction
Creative Brief
Use specific fonts
looking for strong bold lettering
Bright & Fun-filled
Marta Quillen
President
2873 E Marlow Street Orange, CA 94153
marta@larkwoodltdroofing.com
larkwoodltdroofing.com
Was considering having a black business cards so I really wanted to logo to "pop". Even though we are construction I love a card that has personality and fun.

```html
<!DOCTYPE html>
<html lang="en">
<head>
<meta charset="utf-8">
<title>Larkwood Ltd Stationery</title>
<link rel="stylesheet" href="https://fonts.googleapis.com/css2?family=Playfair+Display:wght@700&family=Open+Sans:wght@400;600;700&display=swap">
<style>
:root{
  --bg:#d9c7a6;
  --navy:#0f2a4f;
  --blue:#1f5fa8;
  --sky:#5aa6dd;
  --gold:#f2a31b;
  --ink:#1b2b40;
  --paper:#ffffff;
  --black:#111317;
  --muted:#8a96a6;
  --label:#5b4a30;
}
*{box-sizing:border-box;margin:0;padding:0}
html,body{width:1200px;height:439px;overflow:hidden}
body{background:var(--bg);font-family:"Open Sans",sans-serif;color:var(--ink);position:relative}
.item{position:absolute;box-shadow:0 2px 6px rgba(0,0,0,.28);overflow:hidden}
.label{position:absolute;font-size:7px;color:var(--label);text-align:center}
.brand{display:flex;align-items:center;gap:5px;font-family:"Playfair Display",serif;font-weight:700;color:var(--blue);white-space:nowrap}
.brand .dot{border-radius:50%;background:var(--gold);flex:none}
.wm{position:absolute;border-radius:50%;background:radial-gradient(circle,rgba(90,166,221,.18),rgba(242,163,27,.08) 60%,rgba(255,255,255,0) 72%)}
svg{position:absolute;display:block}

/* cards */
.card{width:125px;height:78px;left:19px}
.card-front{top:110px;background:var(--navy)}
.card-front .left{position:absolute;left:0;top:0;width:52px;height:100%;background:var(--paper);display:flex;align-items:center;justify-content:center}
.card-front .brand{font-size:6px;flex-direction:column;gap:2px}
.card-front .info{position:absolute;left:58px;top:8px;color:#fff;font-size:4.3px;line-height:1.55}
.name{font-weight:700;font-size:6px;color:var(--gold)}
.card-back-a{top:210px;background:var(--navy)}
.card-back-a .info{position:absolute;left:8px;top:8px;color:#fff;font-size:4.3px;line-height:1.55}
.card-back-b{top:310px;background:var(--black)}
.card-back-b .addr{position:absolute;left:0;right:0;bottom:12px;text-align:center;color:#fff;font-size:4.3px}
.card-back-b .brand{position:absolute;left:36px;top:16px;font-size:7px;color:var(--sky)}

/* letterheads */
.letter{top:36px;width:318px;height:372px;background:var(--paper)}
.letter-a{left:156px}
.letter-b{left:504px}
.letter .brand{position:absolute;left:18px;top:18px;font-size:11px}
.letter .brand .dot{width:14px;height:14px}
.letter .contact{position:absolute;left:150px;top:16px;font-size:4.5px;line-height:1.6;color:var(--ink)}
.letter .wm{left:89px;top:110px;width:140px;height:140px}
.letter .foot{position:absolute;left:0;right:0;bottom:8px;text-align:center;color:#fff;font-size:4.5px}

/* envelopes */
.env{left:859px;width:329px;height:130px;background:var(--paper)}
.env-gold{top:40px}
.env-blue{top:112px}
.env-plain{top:192px}
.env-front{top:270px}
.env .brand{position:absolute;font-size:7px}
.env .brand .dot{width:9px;height:9px}
.env-front .addr{position:absolute;left:14px;top:36px;font-size:4.5px;color:var(--ink)}
</style>
</head>
<body>

<!-- business cards -->
<section class="item card card-front">
  <div class="left">
    <div class="brand"><span class="dot" style="width:12px;height:12px"></span>LARKWOOD LTD</div>
  </div>
  <div class="info">
    <div class="name">Marta Quillen</div>
    <div>President</div>
    <div>2873 E Marlow Street</div>
    <div>Orange, CA 94153</div>
    <div>(714) 555-0182</div>
    <div>marta@larkwoodltdroofing.com</div>
    <div>larkwoodltdroofing.com</div>
  </div>
  <svg width="125" height="78" viewBox="0 0 125 78"><path d="M52 78 Q90 60 125 66 L125 78Z" fill="var(--blue)"/><path d="M52 78 Q90 66 125 72 L125 78Z" fill="var(--gold)"/></svg>
</section>
<div class="label" style="left:19px;top:192px;width:125px">Card Front</div>

<section class="item card card-back-a">
  <svg width="125" height="78" viewBox="0 0 125 78"><path d="M60 0 Q85 40 125 30 L125 0Z" fill="var(--blue)"/><path d="M0 78 Q60 50 125 62 L125 78Z" fill="var(--gold)"/></svg>
  <div class="info">
    <div class="name">Marta Quillen</div>
    <div>President</div>
    <div>2873 E Marlow Street</div>
    <div>Orange, CA 94153</div>
    <div>(714) 555-0182</div>
    <div>marta@larkwoodltdroofing.com</div>
  </div>
</section>
<div class="label" style="left:19px;top:292px;width:125px">Card Back A</div>

<section class="item card card-back-b">
  <svg width="125" height="78" viewBox="0 0 125 78"><path d="M0 0 Q40 20 0 50Z" fill="var(--blue)"/><path d="M125 78 Q90 50 125 20Z" fill="var(--gold)"/></svg>
  <div class="brand"><span class="dot" style="width:10px;height:10px"></span>LARKWOOD LTD</div>
  <div class="addr">2873 E Marlow Street Orange, CA 94153</div>
</section>
<div class="label" style="left:19px;top:392px;width:125px">Card Back B</div>

<!-- letterheads -->
<section class="item letter letter-a">
  <div class="brand"><span class="dot"></span>LARKWOOD LTD</div>
  <div class="contact">
    <div>(714) 555-0182</div>
    <div>(714) 555-0190</div>
    <div>marta@larkwoodltdroofing.com</div>
    <div>larkwoodltdroofing.com</div>
  </div>
  <div class="wm" role="img" aria-label="Faint building emblem watermark"></div>
  <svg width="318" height="372" viewBox="0 0 318 372"><path d="M0 338 Q150 318 318 326 L318 372 L0 372Z" fill="var(--gold)"/><path d="M0 345 Q150 328 318 336 L318 372 L0 372Z" fill="var(--blue)"/></svg>
  <div class="foot">2873 E Marlow Street Orange, CA 94153 · larkwoodltdroofing.com</div>
</section>
<div class="label" style="left:156px;top:412px;width:318px">Letterhead A</div>

<section class="item letter letter-b">
  <div class="brand"><span class="dot"></span>LARKWOOD LTD</div>
  <div class="wm" role="img" aria-label="Faint building emblem watermark"></div>
  <svg width="318" height="372" viewBox="0 0 318 372"><path d="M0 332 Q170 350 318 320 L318 372 L0 372Z" fill="var(--sky)"/><path d="M0 342 Q170 360 318 332 L318 372 L0 372Z" fill="var(--blue)"/></svg>
  <div class="foot">2873 E Marlow Street Orange, CA 94153 · (714) 555-0182</div>
</section>
<div class="label" style="left:504px;top:412px;width:318px">Letterhead B</div>

<!-- envelopes -->
<section class="item env env-gold">
  <svg width="329" height="130" viewBox="0 0 329 130"><path d="M0 0 L329 0 L329 20 Q164 70 0 20Z" fill="var(--gold)"/></svg>
  <div class="brand" style="left:130px;top:40px"><span class="dot"></span>LARKWOOD LTD</div>
</section>
<section class="item env env-blue">
  <svg width="329" height="130" viewBox="0 0 329 130"><path d="M0 0 L329 0 L329 20 Q164 70 0 20Z" fill="var(--blue)"/><path d="M0 20 Q164 70 329 20" stroke="var(--sky)" stroke-width="3" fill="none"/></svg>
  <div class="brand" style="left:130px;top:40px"><span class="dot"></span>LARKWOOD LTD</div>
</section>
<section class="item env env-plain">
  <svg width="329" height="130" viewBox="0 0 329 130"><path d="M0 0 L164 55 L329 0" stroke="#d7dde5" stroke-width="1" fill="none"/></svg>
</section>
<section class="item env env-front">
  <div class="brand" style="left:14px;top:14px"><span class="dot"></span>LARKWOOD LTD</div>
  <div class="addr">2873 E Marlow Street Orange, CA 94153</div>
  <svg width="329" height="130" viewBox="0 0 329 130"><path d="M0 118 Q164 104 329 112 L329 130 L0 130Z" fill="var(--blue)"/></svg>
</section>
<div class="label" style="left:859px;top:404px;width:329px">Envelope Set</div>

</body>
</html>
```